domestic violence campaign

To Whom It May Concern:

We are fully aware that domestic violence can enter anyone’s life at any given time. As women we are faced with many demands as mothers, daughters, wives, sisters, providers, and friends. We often lose ourselves and our confidence. Bright Maple Circle (BMC) Transitional Center of Western New York has embarked on a whole new way of intervention and prevention. As a domestic violence survivor I have created a facility and ideals which will enforce a revolution of Domestic Violence victims. For many years, growing up in suburbs of Western New York, I have come to terms with this fight. Domestic Violence can be stopped and prevented. As a domestic violence victim myself, being in live-in facility, as well as six different domestic violence shelters throughout the state, I fled from my domestic violence abuse. Without those temporary facilities, all that comes to my mind is death. They helped me rebuild and save my life but something was missing – zero education, training programs, parenting classes, personal strengthening workshops, on site at all. Considering the limited amount of time (30-45 days in an average shelter) and lack of resources, I was in need of the tools needed to move me from being a victim to having a stable life.
Opening more doors in Western New York is essential with the surrounding agencies and shelters overwhelmed from assisting women of crisis. Many issues have risen, as a result, such as: over-crowding, long waiting lists, and zero educational training with an on-site teaching curriculum. A repeated vicious cycle – victims regressing and not progressing with over 4000 cases of domestic violence reported throughout Erie County. The opening Bright Maple Circle (BMC) Transitional Center of Western New York will provide a 9-24 month live-in facility, along with educational and training programs on-site that will serve as important tools to domestic violence victims. These educational based facilities and services are well needed for Western New York. Our trained certified staff will provide endless help to domestic violence victim. They will feel safe as they rebuild their lives and take advantage of our educational curriculum that has been designed to increase awareness and provide steppingstones to move the victims into confident stable independent human beings. Our clients will receive complete educational training, state testing, parenting classes, as well as strengthening, coping, and developing skills here at our facility. Bright Maple Circle (BMC) Transitional Center is asking for your support.
Sincerely,
Rosalind Pemberton
President and CEO/website bmctcq.org
Bright Maple Circle (BMC) Transitional Center of WNY

Industry/Entity Type

Training

Requirements
Nice to have
• we have already created our T-shirt/we will like for our T-shirt to be the center of the campaign to T-shirt reads
V IOLENCE
O N
W OMEN
S TOPS the campaign is to raise money so we can open doors and save lives

```html
<!DOCTYPE html>
<html lang="en">
<head>
<meta charset="utf-8">
<title>Domestic Violence Campaign – Bright Maple Circle</title>
<link rel="stylesheet" href="https://fonts.googleapis.com/css2?family=Open+Sans:wght@400;600&family=Special+Elite&display=swap">
<style>
  :root {
    --bg-dark: #745859;
    --bg-mid: #836a6b;
    --bg-light: #9a8586;
    --band: #3a2e2e;
    --footer: #715657;
    --text-light: #ffffff;
    --title-red: #a8383b;
    --figure-dark: #0c0a0a;
    --figure-light: #c4c2c2;
  }
  * { margin: 0; padding: 0; box-sizing: border-box; }
  html, body { width: 1200px; height: 1000px; overflow: hidden; }
  body { font-family: "Open Sans", Arial, sans-serif; color: var(--text-light); }

  .poster {
    position: relative;
    width: 1200px;
    height: 1000px;
    overflow: hidden;
    background: linear-gradient(200deg, var(--bg-light) 0%, var(--bg-mid) 40%, var(--bg-dark) 80%);
  }

  .org-name {
    position: absolute;
    left: 30px; top: 22px;
    width: 320px;
    text-align: center;
    font-size: 29px;
    line-height: 40px;
  }

  .donate {
    position: absolute;
    left: 967px; top: 22px;
    font-size: 27px;
    line-height: 36px;
  }

  .headline {
    position: absolute;
    left: 0; right: 0; top: 200px;
    text-align: center;
    padding-left: 100px;
    font-size: 64px;
    font-weight: 400;
    color: var(--title-red);
    text-shadow: 3px 4px 5px rgba(0,0,0,0.45);
  }

  .message {
    position: absolute;
    font-size: 32px;
    white-space: nowrap;
  }
  .message--enter { left: 355px; top: 338px; }
  .message--stop  { left: 70px;  top: 438px; }
  .message--ad    { left: 157px; top: 538px; }
  .message--vows  { left: 329px; top: 623px; }

  .figure-art {
    position: absolute;
    left: 555px; top: 385px;
    width: 645px; height: 430px;
  }

  .slogan-band {
    position: absolute;
    left: 0; top: 815px;
    width: 1200px; height: 120px;
    background: var(--band);
    display: flex;
    align-items: center;
    justify-content: center;
  }
  .slogan {
    font-family: "Special Elite", "Courier New", monospace;
    font-size: 58px;
    letter-spacing: 2px;
    color: var(--text-light);
  }

  .footer-strip {
    position: absolute;
    left: 0; top: 935px;
    width: 1200px; height: 65px;
    background: var(--footer);
  }
</style>
</head>
<body>
  <main class="poster">
    <header>
      <p class="org-name">Bright Maple Circle<br>Transitional<br>Center of<br>Western New York</p>
      <p class="donate">Donate Today<br>bmctcq.org</p>
    </header>

    <h1 class="headline">Domestic Violence</h1>

    <p class="message message--enter">Can enter anyone’s life at any given time</p>
    <p class="message message--stop">Domestic Violence can be stopped or prevented</p>
    <p class="message message--ad">Place your Ad, and speak out take the</p>
    <p class="message message--vows">Vows with BMC</p>

    <svg class="figure-art" viewBox="0 0 645 430" role="img" aria-label="Silhouette of a seated woman hugging her knees, with a pale grey shadow figure behind her">
      <defs>
        <linearGradient id="figureTone" x1="0" y1="0" x2="1" y2="0">
          <stop offset="0" stop-color="var(--figure-light)" stop-opacity="0.85"/>
          <stop offset="0.45" stop-color="var(--figure-light)"/>
          <stop offset="0.6" stop-color="var(--figure-dark)"/>
          <stop offset="1" stop-color="var(--figure-dark)"/>
        </linearGradient>
      </defs>
      <path d="M60 430 C120 330 220 260 330 140 C380 60 450 10 520 5 C600 0 645 40 645 40 L645 430 Z" fill="url(#figureTone)"/>
    </svg>

    <section class="slogan-band">
      <p class="slogan">VIOLENCE ON WOMEN STOPS NOW</p>
    </section>
    <div class="footer-strip"></div>
  </main>
</body>
</html>
```